Author/ Speaker Business Card design

I need a business card designed that will go with the branding that is already on my book and website. I like clean and straightforward, but I am not opposed to something more 'innovative'.

Target Market(s)

Colleges and Universities, educational institutions

Industry/Entity Type

Education

Contact Information for Business Card

Standard size. It should be able to be printed on good quality white or ivory paper.

Font styles to use
Sans Serif

Colors
0355a3

Requirements
Must have
• There's a blue on my website. It should have some blue. My logo is at the top. It should have the logo incorporated somewhere on it. My name, Author | Speaker | Teacher | Trainer, my phone number (+31 64-207 5819), my email address (milo@theboldlearner.example), Social media icons (twitter, Instagram, LinkedIn) with the addresses (twitter @writermilofenwick, Instagram - theboldlearner, LinkedIn - theboldlearner) By they way, the website is www.theboldlearner.example. There is a photo of the book on the website. Also, my full name is Milo Fenwick
Nice to have
• Try to use the font that is on the website and book. Also, if you could get that blue, that would be great.
Should not have
• My photo

```html
<!DOCTYPE html>
<html lang="en">
<head>
<meta charset="utf-8">
<title>The Bold Learner – Business Card</title>
<link rel="stylesheet" href="https://fonts.googleapis.com/css2?family=Montserrat:wght@400;700&family=Questrial&display=swap">
<style>
  :root {
    --brand-blue: #0355a3;
    --card-white: #ffffff;
    --ink-grey: #3a3a3a;
    --backdrop: #e6e8eb;
    --card-shadow: rgba(0, 0, 0, 0.18);
  }
  * { box-sizing: border-box; margin: 0; padding: 0; }
  html, body {
    width: 1200px; height: 900px; overflow: hidden;
    background: var(--backdrop);
  }
  .canvas {
    width: 1200px; height: 900px;
    display: flex; flex-direction: column;
    align-items: center; justify-content: center; gap: 46px;
  }
  .card {
    position: relative;
    width: 660px; height: 377px;
    border-radius: 26px;
    overflow: hidden;
    box-shadow: 0 10px 28px var(--card-shadow);
  }

  /* Front */
  .card--front { background: var(--card-white); }
  .brand-name {
    font-family: "Montserrat", sans-serif;
    font-weight: 700;
    color: var(--brand-blue);
    display: flex; align-items: center; gap: 10px;
    white-space: nowrap;
  }
  .brand-name__dot {
    width: 14px; height: 14px; border-radius: 50%;
    background: currentColor;
  }
  .card--front .brand-name {
    position: absolute; left: 44px; top: 36px;
    font-size: 26px;
  }
  .identity {
    position: absolute; left: 150px; top: 118px;
  }
  .identity__name {
    font-family: "Montserrat", sans-serif;
    font-weight: 700;
    font-size: 32px;
    color: var(--brand-blue);
  }
  .identity__roles {
    margin-top: 6px;
    font-family: "Questrial", sans-serif;
    font-size: 17px;
    color: var(--ink-grey);
    letter-spacing: 0.3px;
  }
  .contacts {
    position: absolute; right: 30px; top: 34px;
    list-style: none;
    font-family: "Questrial", sans-serif;
    font-size: 14px;
    color: var(--ink-grey);
    text-align: right;
  }
  .contacts__item {
    display: flex; align-items: center; justify-content: flex-end;
    gap: 8px; line-height: 24px;
  }
  .contacts__icon { width: 15px; height: 15px; fill: var(--brand-blue); flex: none; }
  .social-band {
    position: absolute; left: 0; right: 0; top: 262px; height: 50px;
    background: var(--brand-blue);
  }
  .social-row {
    position: absolute; left: 0; right: 0;
    display: grid; grid-template-columns: repeat(3, 1fr);
    justify-items: center; align-items: center;
  }
  .social-row--icons { top: 262px; height: 50px; }
  .social-row--handles { top: 312px; height: 65px; }
  .social-icon {
    width: 22px; height: 22px; border-radius: 4px;
    background: var(--card-white);
  }
  .social-handle {
    font-family: "Questrial", sans-serif;
    font-size: 16px;
    color: var(--ink-grey);
  }

  /* Back */
  .card--back {
    background: var(--brand-blue);
    display: flex; align-items: center; justify-content: center;
  }
  .card--back .brand-name {
    color: var(--card-white);
    font-size: 48px;
    gap: 16px;
  }
  .card--back .brand-name__dot { width: 22px; height: 22px; }
</style>
</head>
<body>
<main class="canvas">

  <section class="card card--front" aria-label="Business card front">
    <div class="brand-name"><span class="brand-name__dot"></span>The Bold Learner</div>

    <ul class="contacts">
      <li class="contacts__item">+31 64-207 5819
        <svg class="contacts__icon" viewBox="0 0 24 24" aria-hidden="true"><path d="M6.6 10.8c1.4 2.8 3.8 5.1 6.6 6.6l2.2-2.2c.3-.3.7-.4 1-.2 1.1.4 2.3.6 3.6.6.6 0 1 .4 1 1V20c0 .6-.4 1-1 1C10.6 21 3 13.4 3 4c0-.6.4-1 1-1h3.5c.6 0 1 .4 1 1 0 1.3.2 2.5.6 3.6.1.3 0 .7-.2 1z"/></svg>
      </li>
      <li class="contacts__item">milo@theboldlearner.example
        <svg class="contacts__icon" viewBox="0 0 24 24" aria-hidden="true"><path d="M2 5h20v14H2z" fill="none"/><path d="M2 5h20v2l-10 6L2 7zM2 9l10 6 10-6v10H2z"/></svg>
      </li>
      <li class="contacts__item">www.theboldlearner.example
        <svg class="contacts__icon" viewBox="0 0 24 24" aria-hidden="true"><path d="M12 2a10 10 0 100 20 10 10 0 000-20zm6.9 6h-3a15 15 0 00-1.3-3.6A8 8 0 0118.9 8zM12 4c.8 1.2 1.5 2.5 1.9 4h-3.8c.4-1.5 1.1-2.8 1.9-4zM4.3 14a8 8 0 010-4h3.4a16 16 0 000 4zm.8 2h3a15 15 0 001.3 3.6A8 8 0 015.1 16zM8 8H5.1a8 8 0 014.3-3.6A15 15 0 008 8zm4 12c-.8-1.2-1.5-2.5-1.9-4h3.8c-.4 1.5-1.1 2.8-1.9 4zm2.3-6H9.7a14 14 0 010-4h4.6a14 14 0 010 4zm.3 5.6A15 15 0 0015.9 16h3a8 8 0 01-4.3 3.6zM16.3 14a16 16 0 000-4h3.4a8 8 0 010 4z"/></svg>
      </li>
    </ul>

    <div class="identity">
      <h1 class="identity__name">Milo Fenwick</h1>
      <p class="identity__roles">Author | Speaker | Teacher | Trainer</p>
    </div>

    <div class="social-band"></div>
    <div class="social-row social-row--icons">
      <span class="social-icon"></span>
      <span class="social-icon"></span>
      <span class="social-icon"></span>
    </div>
    <div class="social-row social-row--handles">
      <span class="social-handle">theboldlearner</span>
      <span class="social-handle">@writermilofenwick</span>
      <span class="social-handle">theboldlearner</span>
    </div>
  </section>

  <section class="card card--back" aria-label="Business card back">
    <div class="brand-name"><span class="brand-name__dot"></span>The Bold Learner</div>
  </section>

</main>
</body>
</html>
```